Visitenkarten-Design für Abbruch und Schadstoffsanierungsfirma
Zielgruppe
Wir sind ein Abbruch und Schadstoffsanierungsfirma aus Kassel und suchen einen eleganten unverwechselbaren Design für unsere Visitenkarten.
Zielgruppe: Alle
Aufgabenstellung
Gut lesbar alles

```html
<!DOCTYPE html>
<html lang="de">
<head>
<meta charset="utf-8">
<title>Visitenkarten – Morhaven Bau</title>
<link rel="stylesheet" href="https://fonts.googleapis.com/css2?family=Figtree:ital,wght@0,400;0,600;0,700;1,400&display=swap">
<style>
  :root {
    --backdrop: #333a3d;
    --card-shadow: #262c2f;
    --navy: #0e1124;
    --white: #ffffff;
    --red: #a8281f;
    --band: #d0cdd4;
    --peach: #f0dfd8;
    --ink: #14162a;
  }
  * { margin: 0; padding: 0; box-sizing: border-box; }
  html, body { width: 954px; height: 1200px; overflow: hidden; }
  body {
    background: var(--backdrop);
    font-family: "Figtree", Arial, sans-serif;
    position: relative;
  }
  .card-slot {
    position: absolute;
    width: 440px;
    height: 284px;
  }
  .card-slot::before {
    content: "";
    position: absolute;
    left: 10px; top: 10px;
    width: 440px; height: 284px;
    background: var(--card-shadow);
  }
  .card {
    position: absolute;
    left: 0; top: 0;
    width: 771px;
    height: 498px;
    transform: scale(0.5707);
    transform-origin: 0 0;
    overflow: hidden;
  }
  .slot-front { left: 30px; top: 273px; }
  .slot-back { left: 484px; top: 305px; }
  .slot-back-icons { left: 257px; top: 643px; }

  /* front */
  .card-front { background: var(--navy); color: var(--white); }
  .front-brand {
    position: absolute;
    left: 0; right: 0; top: 215px;
    display: flex; justify-content: center; align-items: center; gap: 18px;
    font-size: 46px; font-weight: 700; letter-spacing: 1px;
  }
  .brand-square { width: 34px; height: 34px; background: currentColor; }
  .front-services {
    position: absolute; left: 0; right: 0; top: 408px;
    text-align: center; font-size: 19px;
  }
  .dot { display: inline-block; margin: 0 10px; font-size: 12px; vertical-align: 3px; }

  /* back */
  .card-back { background: var(--white); color: var(--ink); }
  .card-back .decor { position: absolute; inset: 0; width: 771px; height: 498px; }
  .back-brand {
    position: absolute; left: 72px; top: 118px;
    display: flex; align-items: center; gap: 12px;
    font-size: 27px; font-weight: 700; color: var(--navy); letter-spacing: .5px;
  }
  .back-brand .brand-square { width: 22px; height: 22px; }
  .back-services {
    position: absolute; left: 318px; top: 77px;
    font-size: 18px; color: var(--red);
  }
  .person { position: absolute; left: 457px; top: 262px; }
  .person-name { font-size: 34px; font-weight: 700; line-height: 1; }
  .person-role { font-size: 18px; font-style: italic; color: var(--red); margin-top: 6px; }
  .contact { position: absolute; font-size: 21px; line-height: 30px; list-style: none; }
  .contact-left { left: 75px; top: 345px; }
  .contact-right { left: 457px; top: 372px; }
  .card-icons .contact-left { left: 72px; top: 345px; }
  .card-icons .contact-right { left: 425px; top: 372px; }
  .contact li { display: flex; align-items: flex-start; gap: 9px; }
  .contact .icon { width: 21px; height: 21px; margin-top: 5px; flex: none; }
  .contact .spacer { width: 21px; flex: none; }
</style>
</head>
<body>

<div class="card-slot slot-front">
  <section class="card card-front">
    <div class="front-brand"><span class="brand-square"></span>MORHAVEN BAU</div>
    <p class="front-services">Schadstoffsanierung<span class="dot">■</span>Abbruch<span class="dot">■</span>Entkernen</p>
  </section>
</div>

<div class="card-slot slot-back">
  <section class="card card-back">
    <svg class="decor" viewBox="0 0 771 498" aria-hidden="true">
      <polygon points="697,108 771,0 771,212" fill="var(--peach)"/>
      <polygon points="600,0 771,0 410,498 238,498" fill="var(--band)"/>
    </svg>
    <div class="back-brand"><span class="brand-square"></span>MORHAVEN BAU</div>
    <p class="back-services">Schadstoffsanierung<span class="dot">■</span>Abbruch<span class="dot">■</span>Entkernen</p>
    <div class="person">
      <p class="person-name">Jonas Keller</p>
      <p class="person-role">Geschäftsführer</p>
    </div>
    <ul class="contact contact-left">
      <li>mk-rueckbau.de</li>
      <li>Lindenweg 14,</li>
      <li>34127 Kassel</li>
    </ul>
    <ul class="contact contact-right">
      <li>01572048193</li>
      <li>info@mk-rueckbau.de</li>
    </ul>
  </section>
</div>

<div class="card-slot slot-back-icons">
  <section class="card card-back card-icons">
    <svg class="decor" viewBox="0 0 771 498" aria-hidden="true">
      <polygon points="697,108 771,0 771,212" fill="var(--peach)"/>
      <polygon points="600,0 771,0 410,498 238,498" fill="var(--band)"/>
    </svg>
    <div class="back-brand"><span class="brand-square"></span>MORHAVEN BAU</div>
    <p class="back-services">Schadstoffsanierung<span class="dot">■</span>Abbruch<span class="dot">■</span>Entkernen</p>
    <div class="person">
      <p class="person-name">Jonas Keller</p>
      <p class="person-role">Geschäftsführer</p>
    </div>
    <ul class="contact contact-left">
      <li>
        <svg class="icon" viewBox="0 0 20 20" aria-hidden="true"><circle cx="10" cy="10" r="10" fill="var(--ink)"/><g fill="none" stroke="#fff" stroke-width="1.2"><circle cx="10" cy="10" r="5.5"/><ellipse cx="10" cy="10" rx="2.4" ry="5.5"/><line x1="4.5" y1="10" x2="15.5" y2="10"/></g></svg>
        mk-rueckbau.de
      </li>
      <li>
        <svg class="icon" viewBox="0 0 20 20" aria-hidden="true"><circle cx="10" cy="10" r="10" fill="var(--ink)"/><path d="M10 4.5a3.8 3.8 0 0 1 3.8 3.8c0 2.8-3.8 7-3.8 7s-3.8-4.2-3.8-7A3.8 3.8 0 0 1 10 4.5z" fill="#fff"/><circle cx="10" cy="8.3" r="1.4" fill="var(--ink)"/></svg>
        Lindenweg 14,
      </li>
      <li><span class="spacer"></span>34127 Kassel</li>
    </ul>
    <ul class="contact contact-right">
      <li>
        <svg class="icon" viewBox="0 0 20 20" aria-hidden="true"><circle cx="10" cy="10" r="10" fill="var(--ink)"/><path d="M6.6 5.2l1.8-.4 1 2.4-1.2 1a6.5 6.5 0 0 0 3.6 3.6l1-1.2 2.4 1-.4 1.8c-.2.6-.8.9-1.4.8A9 9 0 0 1 5.8 6.6c-.1-.6.2-1.2.8-1.4z" fill="#fff"/></svg>
        01572048193
      </li>
      <li>
        <svg class="icon" viewBox="0 0 20 20" aria-hidden="true"><circle cx="10" cy="10" r="10" fill="var(--ink)"/><rect x="5" y="6.5" width="10" height="7" rx="1" fill="#fff"/><path d="M5.3 7l4.7 3.6L14.7 7" fill="none" stroke="var(--ink)" stroke-width="1"/></svg>
        info@mk-rueckbau.de
      </li>
    </ul>
  </section>
</div>

</body>
</html>
```